Help a start up law firm make an impression! - Website

We are a property development and conveyancing law firm looking for some to design our website. The initial brief is for 6 pages with scope for on-going work.

Law firms are traditionally quite conservative and we want to break the mold. We want to come across as fun and modern, while still being professional.

A good example is https://quorvantlaw.com.au/. It's professional yet modern.
Updates

Another good site I like in the same industry: https://www.tamberwickconveyancing.com.au/

Target Market(s)

Tech savy home buyers and sellers - generally 30 to 50 years old

Industry/Entity Type

Law Firm

Coding

Coded - Design and coding required

Number of Pages Required

5+ page

Font styles to use
Other font styles liked:
• No idea

Colors
f04a50

Requirements
Must have
• The elements set out in the design brief document

```html
<!DOCTYPE html>
<html lang="en">
<head>
<meta charset="utf-8">
<title>HartwellLaw — The Property Law Experts</title>
<link href="https://fonts.googleapis.com/css2?family=Abril+Fatface&family=Open+Sans:ital,wght@0,400;0,600;0,700;1,400;1,600&display=swap" rel="stylesheet">
<style>
:root{
  --pink:#d5405d;
  --pink-dark:#b8304b;
  --pink-soft:#e06a80;
  --ink:#1b1b1b;
  --text:#555;
  --white:#fff;
}
*{box-sizing:border-box;margin:0;padding:0}
html,body{width:1200px;height:3774px;overflow:hidden}
body{font-family:'Open Sans',Arial,sans-serif;color:var(--text);background:#fff;position:relative}
.display{font-family:'Abril Fatface',Georgia,serif;font-weight:400}
.wrap{width:1050px;margin:0 auto;position:relative;height:100%}
svg{display:block}

/* header */
.site-header{height:105px}
.logo{position:absolute;left:0;top:30px;font-family:'Abril Fatface',Georgia,serif;font-size:40px;color:var(--ink);letter-spacing:.5px}
.header-call{position:absolute;right:0;top:26px;display:flex;gap:14px;align-items:center}
.header-call .ic{width:42px;height:42px}
.header-call small{display:block;font-size:17px;font-weight:600;color:var(--ink)}
.header-call strong{font-family:'Abril Fatface',Georgia,serif;font-size:30px;color:var(--pink);letter-spacing:1px}

/* nav */
.main-nav{height:63px;background:var(--pink)}
.main-nav ul{list-style:none;display:flex;height:63px}
.main-nav li{font-size:16px;color:#fff;text-transform:uppercase;line-height:63px;padding:0 34px}
.main-nav li.active{background:#111}
.main-nav .search{position:absolute;right:18px;top:20px}

/* hero */
.hero{height:519px;background:linear-gradient(180deg,#6d6a72 0%,#44424a 55%,#2a2930 100%)}
.hero h1{position:absolute;left:0;top:395px;color:#fff;font-size:37px;font-weight:600;letter-spacing:.5px}
.hero p{position:absolute;left:0;top:450px;color:#eee;font-size:14px}

/* welcome */
.welcome{height:365px;background:var(--pink);color:#fff}
.welcome h3{position:absolute;top:40px;font-size:22px;color:#111}
.welcome h2{position:absolute;top:68px;font-size:44px}
.welcome .copy{position:absolute;top:145px;width:600px;font-size:13px;line-height:28px}
.welcome .copy p+p{margin-top:8px}

.contact-card{position:absolute;left:730px;top:486px;width:322px;height:508px;background:#fff;box-shadow:0 4px 18px rgba(0,0,0,.2);z-index:2}
.contact-card .cap{height:102px;position:relative}
.contact-card .cap span{position:absolute;top:20px;width:100%;text-align:center;color:#fff;font-family:'Abril Fatface',Georgia,serif;font-size:28px}
.contact-card .intro{text-align:center;font-style:italic;font-size:13px;line-height:24px;color:#333;padding:8px 22px 12px}
.field{margin:0 26px 10px;height:45px;background:#ececec;position:relative;font-size:13px;color:#444;padding:13px 0 0 16px}
.field.msg{height:82px}
.field .tag{position:absolute;right:0;top:0;width:42px;height:100%;background:var(--pink);display:flex;align-items:center;justify-content:center}
.btn{display:inline-block;background:var(--pink);color:#fff;font-family:'Abril Fatface',Georgia,serif;letter-spacing:2px;text-transform:uppercase;border-radius:6px;text-align:center}
.contact-card .btn{display:block;width:176px;height:56px;line-height:56px;font-size:20px;margin:12px auto 0}

/* what we do */
.features{height:495px;background:#fff}
.eyebrow{position:absolute;width:100%;text-align:center;font-family:'Abril Fatface',Georgia,serif;font-size:21px;color:#111}
.section-title{position:absolute;width:100%;text-align:center;font-family:'Abril Fatface',Georgia,serif;font-size:40px;font-weight:400;color:var(--pink)}
.features .eyebrow{top:60px}
.features .section-title{top:90px}
.feature-cards{position:absolute;top:218px;left:0;display:flex;gap:17px}
.feature{width:250px;height:214px;border:2px solid #e2e2e2;border-top:4px solid #e2e2e2;background:#fff;text-align:center;position:relative;padding-top:76px}
.feature.active{border-color:var(--pink)}
.feature .badge{position:absolute;left:73px;top:-48px;width:100px;height:100px;border-radius:50%;background:#bdbdbd;display:flex;align-items:center;justify-content:center}
.feature.active .badge{background:var(--pink)}
.feature h4{font-family:'Abril Fatface',Georgia,serif;font-weight:400;font-size:16px;color:#222;letter-spacing:1px;line-height:21px;text-transform:uppercase}
.feature.active h4{color:var(--pink)}
.feature p{font-size:12.5px;line-height:20px;padding:8px 14px 0}

/* services */
.services{height:823px;background:linear-gradient(180deg,var(--pink) 0,var(--pink) 390px,#fff 390px)}
.services .eyebrow{top:62px}
.services .section-title{top:90px;color:#fff}
.services .lead{position:absolute;top:156px;left:130px;width:790px;text-align:center;color:#fff;font-style:italic;font-size:15px;line-height:27px}
.service{position:absolute;top:232px;left:0;width:494px}
.service.dev{left:546px}
.service .photo{height:272px;border:7px solid #fff}
.service .photo.a{background:linear-gradient(135deg,#e8e8ea,#9aa0a8 50%,#4f545c)}
.service .photo.b{background:linear-gradient(135deg,#dfe8f2,#b9c4d2 50%,#707c8e)}
.service h3{margin-top:20px;font-family:'Abril Fatface',Georgia,serif;font-weight:400;font-size:44px;line-height:60px;color:#111;letter-spacing:2px}
.service p{font-size:13px;line-height:25px;margin-top:10px}
.service .btn{margin-top:18px;width:208px;height:56px;line-height:56px;font-size:20px}

/* cta */
.cta{height:468px;background:linear-gradient(180deg,#2a2a2e,#141416);text-align:center;color:#fff}
.cta h2{position:absolute;top:90px;width:100%;font-family:'Abril Fatface',Georgia,serif;font-weight:400;font-size:44px;line-height:62px;letter-spacing:1px}
.cta .call{position:absolute;top:235px;width:100%;display:flex;justify-content:center;align-items:center;gap:20px}
.cta .call span{color:var(--pink);font-size:25px}
.cta .call strong{font-family:'Abril Fatface',Georgia,serif;font-weight:400;color:var(--pink);font-size:42px;letter-spacing:2px}
.cta .btn{position:absolute;top:323px;left:420px;width:210px;height:58px;line-height:58px;font-size:19px}

/* blog */
.blog{height:596px}
.blog .eyebrow{top:50px}
.blog .section-title{top:80px}
.post{position:absolute;top:171px;width:330px;height:362px;background:#fff;box-shadow:0 2px 10px rgba(0,0,0,.12)}
.post .thumb{height:175px;background:linear-gradient(135deg,#c8c8c8,#5c5f66)}
.post h5{font-size:17px;font-style:italic;font-weight:600;color:#111;padding:20px 20px 0}
.post .date{display:inline-block;background:var(--pink);color:#fff;font-family:'Abril Fatface',Georgia,serif;font-size:18px;letter-spacing:1px;padding:8px 16px;margin:14px 0 0 20px;border-radius:3px}
.post p{font-size:13px;line-height:25px;padding:16px 20px 0}
.post.featured{background:linear-gradient(160deg,var(--pink-soft),var(--pink-dark))}
.post.featured .bubble{position:absolute;left:20px;top:-20px;width:46px;height:46px;border-radius:50%;background:var(--pink);border:3px solid #fff;display:flex;align-items:center;justify-content:center}
.post.featured .date{margin-top:150px;background:var(--pink-dark)}
.post.featured h5,.post.featured p{color:#fff}
.post.featured h5{padding-top:12px}
.post.featured p{padding-top:8px;opacity:.9}

/* footer */
.site-footer{height:290px;background:linear-gradient(180deg,#2d2b2f,#1a191c);border-top:6px solid var(--pink);color:#ddd}
.site-footer .logo{top:100px;color:#fff;font-size:36px}
.social{position:absolute;top:160px;left:32px;display:flex;gap:12px}
.social span{width:42px;height:42px;border-radius:50%;background:var(--pink)}
.fcol{position:absolute;top:26px}
.fcol h6{font-family:'Abril Fatface',Georgia,serif;font-size:18px;letter-spacing:1.5px;color:var(--pink);font-weight:400;text-transform:uppercase}
.fcol ul{list-style:none;margin-top:12px}
.fcol li{font-size:13px;line-height:31px;padding-left:22px;position:relative}
.fcol li:before{content:"";position:absolute;left:0;top:12px;width:7px;height:7px;border-radius:50%;background:var(--pink)}
.fcol.sitemap{left:262px}
.fcol.contact{left:530px;width:250px}
.contact-line{display:flex;gap:14px;font-size:13px;line-height:22px;margin-top:16px}
.contact-line svg{flex:none;margin-top:2px}
.fcol.news{left:792px;width:250px}
.fcol.news p{font-size:13px;line-height:23px;margin-top:12px}
.email-field{margin-top:12px;height:40px;background:#fff;color:#666;font-size:13px;padding:10px 12px;position:relative}
.email-field svg{position:absolute;right:10px;top:13px}
.fcol.news .btn{margin-top:12px;width:175px;height:40px;line-height:40px;font-size:17px;border-radius:3px}
.copyright{height:50px;background:var(--pink);color:#fff;text-align:center;font-size:13px;line-height:50px}
</style>
</head>
<body>

<header class="site-header">
  <div class="wrap">
    <div class="logo">HartwellLaw</div>
    <div class="header-call">
      <svg class="ic" viewBox="0 0 42 42"><circle cx="21" cy="21" r="21" fill="#d5405d"/><path d="M14 12c2-1 3 0 4 2l1 3c0 1-1 2-2 3 1 3 3 5 6 6 1-1 2-2 3-2l3 1c2 1 3 2 2 4-1 2-3 3-5 3-7-1-13-7-14-14 0-2 1-4 2-6z" fill="#fff"/></svg>
      <div><small>Call Our Experts Today :</small><strong>1.800.555.0199</strong></div>
    </div>
  </div>
</header>

<nav class="main-nav">
  <div class="wrap">
    <ul>
      <li class="active">Home</li><li>Conveyancing</li><li>Property Development</li><li>News</li><li>About Us</li><li>Contact Us</li>
    </ul>
    <svg class="search" width="22" height="22" viewBox="0 0 22 22"><circle cx="9" cy="9" r="7" fill="none" stroke="#fff" stroke-width="3"/><path d="M14 14l6 6" stroke="#fff" stroke-width="3" stroke-linecap="round"/></svg>
  </div>
</nav>

<section class="hero" role="img" aria-label="Photo of business people talking in a bright office lobby">
  <div class="wrap">
    <h1>THE PROPERTY LAW EXPERTS</h1>
    <p>Unrivaled response times, fixed fee options and experienced property lawyers</p>
  </div>
</section>

<section class="welcome">
  <div class="wrap">
    <h3 class="display">Welcome To</h3>
    <h2 class="display">HartwellLaw</h2>
    <div class="copy">
      <p>At Hartwell Property Group, We have a rich history of helping our clients succeed by creating high quality investment opportunities in development sites, new projects or residential properties.</p>
      <p>We try harder. We work smarter. We avoid pitfalls by collaborating with a range of professional stakeholders who can identify lucrative building sites with strong development potential for residential and mixed-used developments. You do what you do best.</p>
    </div>
  </div>
</section>

<aside class="contact-card">
  <div class="cap">
    <svg width="322" height="102" viewBox="0 0 322 102"><path d="M0 0H322V62L161 102 0 62Z" fill="#d5405d"/></svg>
    <span>Get In Touch</span>
  </div>
  <p class="intro">We take great pride in using our expertise for you and look forward to hearing from you.</p>
  <div class="field">Name *<span class="tag"><svg width="16" height="16" viewBox="0 0 16 16"><circle cx="8" cy="5" r="4" fill="#fff"/><path d="M0 16c0-5 4-7 8-7s8 2 8 7z" fill="#fff"/></svg></span></div>
  <div class="field">Email *<span class="tag"><svg width="18" height="14" viewBox="0 0 18 14"><rect width="18" height="14" rx="2" fill="#fff"/><path d="M1 2l8 6 8-6" fill="none" stroke="#d5405d" stroke-width="1.6"/></svg></span></div>
  <div class="field">Subject *<span class="tag"><svg width="14" height="9" viewBox="0 0 14 9"><path d="M0 0h14L7 9z" fill="#fff"/></svg></span></div>
  <div class="field msg">Message *<span class="tag"><svg width="20" height="18" viewBox="0 0 20 18"><path d="M2 1h16a1 1 0 011 1v10a1 1 0 01-1 1H8l-5 4v-4H2a1 1 0 01-1-1V2a1 1 0 011-1z" fill="#fff"/></svg></span></div>
  <span class="btn">Submit</span>
</aside>

<section class="features">
  <div class="wrap">
    <div class="eyebrow">Why Choose Us</div>
    <h2 class="section-title">What We Do</h2>
    <div class="feature-cards">
      <div class="feature">
        <div class="badge"><svg width="44" height="44" viewBox="0 0 44 44"><path d="M6 6v32h32" fill="none" stroke="#fff" stroke-width="4"/><path d="M12 12l20 20M26 32h6v-6" fill="none" stroke="#fff" stroke-width="4"/></svg></div>
        <h4>Cost<br>Certainty</h4>
        <p>Lorem Ipsum is simple dummy text of print and type setting industry of the print text.</p>
      </div>
      <div class="feature active">
        <div class="badge"><svg width="48" height="44" viewBox="0 0 48 44"><circle cx="14" cy="8" r="5" fill="#fff"/><circle cx="34" cy="8" r="5" fill="#fff"/><rect x="6" y="20" width="36" height="5" fill="#fff"/><path d="M10 25v17M38 25v17M24 25v17" stroke="#fff" stroke-width="4"/></svg></div>
        <h4>Expert<br>Lawyers</h4>
        <p>Lorem Ipsum is simple dummy text of print and type setting industry of the print text.</p>
      </div>
      <div class="feature">
        <div class="badge"><svg width="48" height="42" viewBox="0 0 48 42"><rect x="4" y="4" width="40" height="26" rx="2" fill="none" stroke="#fff" stroke-width="4"/><path d="M18 38h12M24 30v8" stroke="#fff" stroke-width="4"/></svg></div>
        <h4>Responsive<br>Service</h4>
        <p>Lorem Ipsum is simple dummy text of print and type setting industry of the print text.</p>
      </div>
      <div class="feature">
        <div class="badge"><svg width="40" height="46" viewBox="0 0 40 46"><rect x="4" y="3" width="30" height="40" fill="none" stroke="#fff" stroke-width="4"/><path d="M11 14h16M11 22h16M11 30h10" stroke="#fff" stroke-width="3"/></svg></div>
        <h4>Commercial<br>Advice</h4>
        <p>Lorem Ipsum is simple dummy text of print and type setting industry of the print text.</p>
      </div>
    </div>
  </div>
</section>

<section class="services">
  <div class="wrap">
    <div class="eyebrow">We Provide You</div>
    <h2 class="section-title">Our Best Services</h2>
    <p class="lead">Lorem Ipsum is simply dummy text of the printing and typesetting industry. Lorem Ipsum has been the industry's standard dummy text ever since the.</p>
    <article class="service">
      <div class="photo a" role="img" aria-label="Photo of business people shaking hands in front of city towers"></div>
      <h3>Conveyancing</h3>
      <p>Lorem Ipsum is simply dummy text of the printing and typesetting industry. Lorem Ipsum has been the industry's standard dummy text ever since the 1500s, when an unknown printer took a galley of type and scrambled it to make a type specimen book. It has survived not only.</p>
      <span class="btn">Learn Morn</span>
    </article>
    <article class="service dev">
      <div class="photo b" role="img" aria-label="Photo of a large business meeting around a conference table"></div>
      <h3>Development Law</h3>
      <p>Lorem Ipsum is simply dummy text of the printing and typesetting industry. Lorem Ipsum has been the industry's standard dummy text ever since the 1500s, when an unknown printer took a galley of type and scrambled it to make a type specimen book. It has survived not only.</p>
      <span class="btn">Learn Morn</span>
    </article>
  </div>
</section>

<section class="cta" role="img" aria-label="Dark photo of a city skyline seen from an office">
  <div class="wrap">
    <h2>Buying Or Selling ? Go With The<br>Conveyancing Experts</h2>
    <div class="call">
      <span>Call Our Experts Today :</span>
      <svg width="64" height="64" viewBox="0 0 42 42"><circle cx="21" cy="21" r="21" fill="#d5405d"/><path d="M14 12c2-1 3 0 4 2l1 3c0 1-1 2-2 3 1 3 3 5 6 6 1-1 2-2 3-2l3 1c2 1 3 2 2 4-1 2-3 3-5 3-7-1-13-7-14-14 0-2 1-4 2-6z" fill="#fff"/></svg>
      <strong>1.800.555.0199</strong>
    </div>
    <span class="btn">Contact Us</span>
  </div>
</section>

<section class="blog">
  <div class="wrap">
    <div class="eyebrow">Recent</div>
    <h2 class="section-title">Blog Post</h2>
    <article class="post featured" style="left:0" role="img" aria-label="Pink tinted photo of a person writing at a desk">
      <span class="bubble"><svg width="20" height="18" viewBox="0 0 20 18"><path d="M2 1h16a1 1 0 011 1v10a1 1 0 01-1 1H8l-5 4v-4H2a1 1 0 01-1-1V2a1 1 0 011-1z" fill="#fff"/></svg></span>
      <span class="date">10 Sep 2017</span>
      <h5>Blog Post Title.</h5>
      <p>What goes into a blog post? Helpful, industry-specific content that: 1) gives readers a useful takeaway, and 2)...</p>
    </article>
    <article class="post" style="left:355px">
      <div class="thumb" role="img" aria-label="Photo of a man working on a laptop"></div>
      <h5>Real estate laws on the move</h5>
      <span class="date">02 July 2015</span>
      <p>Lorem Ipsum is simply dummy text of the printing and typesetting industry....</p>
    </article>
    <article class="post" style="left:710px">
      <div class="thumb" role="img" aria-label="Photo of colleagues meeting around a table"></div>
      <h5>Private equity firm takes control</h5>
      <span class="date">02 July 2015</span>
      <p>Lorem Ipsum is simply dummy text of the printing and typesetting industry....</p>
    </article>
  </div>
</section>

<footer class="site-footer">
  <div class="wrap">
    <div class="logo">HartwellLaw</div>
    <div class="social"><span></span><span></span><span></span><span></span></div>
    <div class="fcol sitemap">
      <h6>Sitemap</h6>
      <ul><li>Home</li><li>Conveyancing</li><li>Property Development</li><li>News</li><li>About Us</li><li>Contact</li></ul>
    </div>
    <div class="fcol contact">
      <h6>Contact Us</h6>
      <div class="contact-line"><svg width="16" height="22" viewBox="0 0 16 22"><path d="M8 0a8 8 0 018 8c0 6-8 14-8 14S0 14 0 8a8 8 0 018-8z" fill="#d5405d"/><circle cx="8" cy="8" r="3" fill="#222"/></svg><span>Kestrel &amp; Vale Corporate<br>Office 27 Larkspur Avenue<br>Brookfield, NY 10482</span></div>
      <div class="contact-line"><svg width="18" height="18" viewBox="0 0 42 42"><path d="M8 4c4-2 6 0 8 4l2 6c0 2-2 4-4 6 2 6 6 10 12 12 2-2 4-4 6-4l6 2c4 2 6 4 4 8-2 4-6 6-10 6C18 42 2 26 0 12c0-4 4-6 8-8z" fill="#d5405d"/></svg><span>1.800.555.0199</span></div>
      <div class="contact-line"><svg width="18" height="14" viewBox="0 0 18 14"><rect width="18" height="14" rx="2" fill="#d5405d"/><path d="M1 2l8 6 8-6" fill="none" stroke="#222" stroke-width="1.6"/></svg><span>Corporate@kestrelvale.com</span></div>
    </div>
    <div class="fcol news">
      <h6>Newsletter</h6>
      <p>Would you like to receive exclusive access to articles, white papers and our regular monthly newsletter?</p>
      <div class="email-field">Enter Email *<svg width="16" height="12" viewBox="0 0 18 14"><rect width="18" height="14" rx="2" fill="#d5405d"/><path d="M1 2l8 6 8-6" fill="none" stroke="#fff" stroke-width="1.6"/></svg></div>
      <span class="btn">Subscribe</span>
    </div>
  </div>
</footer>
<div class="copyright">©HartwellLaw - 2017 | All Rights Reserved</div>

</body>
</html>
```